Dr Selwyn aesthetics - Radiance Refined

I need a logo design for a new aesthetics business in London. I am specialised in Botox, Dermal Fillers & Skin Pigmentation treatment. The slogan is Radiance Refined. I would like some of the writing on the card to be embossed. I would like a very elegant design with the following detail:

1. White and gray scale background. For the font colour try gold OR silver shades.
2. The business involves working on the face mostly. Anything that can be done with letter 'M'? Or any other logo?
3. The front of the card should have Dr Selwyn Aesthetics and the slogan 'Radiance Refined'. The back should have my full name (Dr Selwyn Tarkett), qualifications (MBBS MSC BSC), my website (www.thebrindlecliniccollective.example), telephone number & email.
4. The back should also say treatments offered: ANTI-WRINKLE INJECTIONS. DERMAL FILLERS, LIP ENHANCEMENT, HYPERHYDROSIS. SKIN PIGMENTATION

Thank you very much
Updates

Project Deadline Extended
Reason: Delays in market research response. I would be grateful for an extension please. Many thanks

Target Market(s)

Female and male aged 18 and above

Industry/Entity Type

Business

Contact Information for Business Card

Elegant design. Square corners. British standard size. Horizontal design. Should contain the slogan, contact details.

Font styles to use
Script

Colors
c9c9c9
fbed22
ffffff
f5f5f5
000000

Requirements
Must have
• All that's mentioned above
Nice to have
• A logo with the outline of a female face. Or anything that can be done with the letter M of Selwyn.
Should not have
• No colours like green / purple / orange

```html
<!DOCTYPE html>
<html lang="en">
<head>
<meta charset="utf-8">
<title>Dr Selwyn Aesthetics – Business Card</title>
<link href="https://fonts.googleapis.com/css2?family=Great+Vibes&family=Questrial&display=swap" rel="stylesheet">
<style>
  :root {
    --backdrop: #2b2b2b;
    --card: #6d6d6d;
    --ink: #ececec;
    --ink-soft: #dcdcdc;
    --rule: rgba(236, 236, 236, 0.55);
  }
  * { box-sizing: border-box; margin: 0; padding: 0; }
  html, body {
    width: 1200px; height: 1098px; overflow: hidden;
    background: var(--backdrop);
  }
  .canvas {
    width: 1200px; height: 1098px;
    display: flex; flex-direction: column; align-items: center; justify-content: center;
    gap: 44px;
  }
  .card {
    position: relative;
    width: 780px; height: 505px;
    background: var(--card);
    color: var(--ink);
    font-family: "Questrial", sans-serif;
    overflow: hidden;
  }

  /* Wordmark shared */
  .wordmark { display: flex; align-items: center; }
  .wordmark__circle {
    border: 2px solid var(--ink);
    border-radius: 50%;
    flex: none;
  }
  .wordmark__text { display: flex; flex-direction: column; align-items: flex-end; }
  .wordmark__name {
    font-family: "Great Vibes", cursive;
    font-weight: 400;
    color: var(--ink);
    line-height: 1;
    white-space: nowrap;
  }
  .wordmark__slogan {
    font-family: "Great Vibes", cursive;
    color: var(--ink);
    line-height: 1;
    white-space: nowrap;
  }

  /* Back */
  .card--back .wordmark {
    position: absolute; left: 56px; top: 44px; gap: 26px;
  }
  .card--back .wordmark__circle { width: 88px; height: 88px; }
  .card--back .wordmark__name { font-size: 56px; }
  .card--back .wordmark__slogan { font-size: 24px; margin-top: 0; margin-right: 6px; }

  .treatments {
    position: absolute; left: 40px; right: 40px; top: 172px;
    text-align: center;
  }
  .treatments__rule {
    height: 1px;
    background: linear-gradient(90deg, transparent, var(--rule) 20%, var(--rule) 80%, transparent);
  }
  .treatments__list {
    padding: 12px 0 14px;
    font-size: 23px; line-height: 1.4; letter-spacing: 0.3px;
    color: var(--ink);
    white-space: nowrap;
  }

  .contact {
    position: absolute; right: 52px; top: 296px;
    text-align: right;
    color: var(--ink-soft);
  }
  .contact__name {
    font-size: 20px; letter-spacing: 0.5px; color: var(--ink);
    white-space: nowrap;
  }
  .contact__name strong { font-weight: 400; -webkit-text-stroke: 0.6px var(--ink); }
  .contact__quals { font-size: 14px; margin-left: 6px; }
  .contact__row {
    display: flex; align-items: center; justify-content: flex-end; gap: 10px;
    font-size: 18px; margin-top: 8px; white-space: nowrap;
  }
  .contact__row--gap { margin-top: 30px; }
  .contact__icon { width: 16px; height: 16px; flex: none; }

  /* Front */
  .card--front .wordmark {
    position: absolute; left: 50%; top: 50%;
    transform: translate(-50%, -50%);
    gap: 28px;
  }
  .card--front .wordmark__circle { width: 124px; height: 124px; }
  .card--front .wordmark__name { font-size: 66px; }
  .card--front .wordmark__slogan { font-size: 28px; margin-top: 0; margin-right: 8px; }
</style>
</head>
<body>
<main class="canvas">

  <section class="card card--back" aria-label="Card back">
    <div class="wordmark">
      <span class="wordmark__circle" aria-hidden="true"></span>
      <div class="wordmark__text">
        <span class="wordmark__name">Dr Selwyn Aesthetics</span>
        <span class="wordmark__slogan">Radiance Refined</span>
      </div>
    </div>

    <div class="treatments">
      <div class="treatments__rule"></div>
      <p class="treatments__list">
        Anti-Wrinkle Injections - Dermal Fillers - Lip Enhancement<br>
        Hyperhydrosis - Skin Pigmentation
      </p>
      <div class="treatments__rule"></div>
    </div>

    <div class="contact">
      <p class="contact__name"><strong>Dr Selwyn Tarkett</strong><span class="contact__quals">MBBS MSC BSC</span></p>
      <p class="contact__row">123 456 7890
        <svg class="contact__icon" viewBox="0 0 24 24" aria-hidden="true"><path fill="#ececec" d="M6.6 10.8a15.1 15.1 0 0 0 6.6 6.6l2.2-2.2c.3-.3.7-.4 1-.2 1.1.4 2.3.6 3.6.6.6 0 1 .4 1 1V20c0 .6-.4 1-1 1A17 17 0 0 1 3 4c0-.6.4-1 1-1h3.5c.6 0 1 .4 1 1 0 1.3.2 2.5.6 3.6.1.3 0 .7-.2 1z"/></svg>
      </p>
      <p class="contact__row contact__row--gap">info@thebrindlecliniccollective.example
        <svg class="contact__icon" viewBox="0 0 24 24" aria-hidden="true"><rect x="2" y="5" width="20" height="14" rx="1.5" fill="#ececec"/><path d="M3 6l9 7 9-7" fill="none" stroke="#6d6d6d" stroke-width="1.6"/></svg>
      </p>
      <p class="contact__row">www.thebrindlecliniccollective.example
        <svg class="contact__icon" viewBox="0 0 24 24" aria-hidden="true"><circle cx="12" cy="12" r="10" fill="#ececec"/><path d="M2 12h20M12 2c3 3 3 17 0 20M12 2c-3 3-3 17 0 20" fill="none" stroke="#6d6d6d" stroke-width="1.4"/></svg>
      </p>
    </div>
  </section>

  <section class="card card--front" aria-label="Card front">
    <div class="wordmark">
      <span class="wordmark__circle" aria-hidden="true"></span>
      <div class="wordmark__text">
        <span class="wordmark__name">Dr Selwyn Aesthetics</span>
        <span class="wordmark__slogan">Radiance Refined</span>
      </div>
    </div>
  </section>

</main>
</body>
</html>
```